Business card update

Opening a subsidiary of my company in the USA and need to update my logo.
Updates

I made a mistake on my briefing. It's only the business card. Thanks for alerting me on the mistake.

All the best

Gustavo

Target Market(s)

We are an Executive Search company and our target audience are executives in large corporations.

Industry/Entity Type

Business

Requirements
Must have
• Keep the logo. In the US the company is called Dario Kellner Executive Search.

```html
<!DOCTYPE html>
<html lang="en">
<head>
<meta charset="utf-8">
<title>Gustavo D. Kellner – Business Card</title>
<link rel="stylesheet" href="https://fonts.googleapis.com/css2?family=Josefin+Sans:wght@400;600&display=swap">
<style>
  :root {
    --backdrop: #2b2b2b;
    --card-light: #f4f4f4;
    --card-mid: #e2e2e2;
    --teal: #1f93a4;
    --ink: #3a3a3a;
    --ink-soft: #444444;
  }
  * { margin: 0; padding: 0; box-sizing: border-box; }
  html, body {
    width: 1200px;
    height: 852px;
    overflow: hidden;
    background: var(--backdrop);
  }
  .business-card {
    position: absolute;
    left: 50px;
    top: 105px;
    width: 1100px;
    height: 642px;
    overflow: hidden;
    background: radial-gradient(ellipse at 55% 35%, var(--card-light) 0%, var(--card-mid) 100%);
    font-family: "Josefin Sans", sans-serif;
    color: var(--ink);
  }
  .card-sweeps {
    position: absolute;
    inset: 0;
    width: 100%;
    height: 100%;
  }
  .brand-mark {
    position: absolute;
    left: 70px;
    top: 250px;
    display: flex;
    align-items: center;
    gap: 22px;
  }
  .brand-dot {
    width: 54px;
    height: 54px;
    border-radius: 50%;
    background: var(--teal);
    flex: none;
  }
  .brand-name {
    font-weight: 600;
    font-size: 40px;
    line-height: 1.15;
    color: var(--teal);
  }
  .holder-name {
    position: absolute;
    right: 69px;
    top: 120px;
    font-weight: 600;
    font-size: 54px;
    letter-spacing: 0.5px;
    text-transform: uppercase;
    color: var(--ink);
    text-shadow: 0 2px 3px rgba(0,0,0,0.25);
    white-space: nowrap;
  }
  .holder-name .initial { color: var(--teal); }
  .contact-block {
    position: absolute;
    right: 72px;
    text-align: right;
    font-weight: 400;
    font-size: 38px;
    line-height: 44px;
    color: var(--ink-soft);
    white-space: nowrap;
  }
  .contact-address { top: 265px; }
  .contact-online { top: 478px; }
</style>
</head>
<body>
  <section class="business-card">
    <svg class="card-sweeps" viewBox="0 0 1100 642" aria-hidden="true">
      <path d="M300 0 C 520 160, 640 420, 620 642" fill="none" stroke="#ffffff" stroke-opacity="0.7" stroke-width="3"/>
      <path d="M420 0 C 700 120, 900 330, 1100 380" fill="none" stroke="#ffffff" stroke-opacity="0.6" stroke-width="2"/>
      <path d="M0 520 C 300 430, 700 470, 1100 620" fill="none" stroke="#ffffff" stroke-opacity="0.5" stroke-width="2"/>
    </svg>

    <div class="brand-mark">
      <span class="brand-dot"></span>
      <p class="brand-name">Dario Kellner<br>Executive Search</p>
    </div>

    <h1 class="holder-name">Gustavo <span class="initial">D. K</span>ellner</h1>

    <address class="contact-block contact-address">
      14780 Harbor View<br>
      Blvd Suite 300<br>
      Coral Point FL 33190<br>
      305 555-0148
    </address>

    <p class="contact-block contact-online">
      www.dkexecutivesearch.com<br>
      gkellner@dkexecutivesearch.com
    </p>
  </section>
</body>
</html>
```